Flyer Design Project for lawn care business

I need a flyer designed for my lawn care business, "Hadley's Groundskeeping Services".  It is a family owned small landscaping company. I was thinking something that I can print  2- 3 per page.
I have  2 different logos I can upload to give an idea.  I have seen some I like that are colorfull with neat graphics but I also like some that are simple and elegant.  I would like something that catches your eye and looks professionaly done.

Target Market(s)
Homeowners in Durham, North Carolina with homes usually valued $200,000 or more.
Industry/Entity Type
Landscaping
Requirements
Must have
- I would like the address of my website listed on it, www.hadleygroundskeepingservices.example
I would like for it to say somewhere, 50% off first service with seasonal service.
Not sure if I want to list some of the services that I offer or just say full service lawn care.
Nice to have
- I have a logo with a bull pushing a lawn mower.  I live in Durham, NC also known as the Bull City.  I am not in love with the logo so feel free to change it or not use it at all.

```html
<!DOCTYPE html>
<html lang="en">
<head>
<meta charset="utf-8">
<title>Hadley's Groundskeeping Services – Flyer</title>
<link rel="stylesheet" href="https://fonts.googleapis.com/css2?family=Poppins:wght@500;600;700&display=swap">
<style>
  :root {
    --soil-dark: #3b2419;
    --soil-mid: #5a3a2a;
    --grass-light: #7ed321;
    --grass-deep: #3f8f12;
    --accent-green: #6ddc14;
    --text-white: #ffffff;
    --page-bg: #ffffff;
  }
  html, body {
    margin: 0;
    padding: 0;
    width: 932px;
    height: 1200px;
    overflow: hidden;
    background: var(--page-bg);
  }
  .flyer {
    display: block;
    width: 932px;
    height: 1200px;
    font-family: "Poppins", sans-serif;
  }
  .brand-name { fill: var(--text-white); font-weight: 700; font-size: 128px; }
  .tagline { fill: var(--accent-green); font-weight: 600; font-size: 54px; }
  .web-address { fill: var(--text-white); font-weight: 600; font-size: 34px; }
  .offer-big { fill: var(--text-white); font-weight: 700; font-size: 150px; }
  .offer-line { fill: var(--text-white); font-weight: 600; font-size: 88px; }
</style>
</head>
<body>
<svg class="flyer" viewBox="0 0 932 1200" xmlns="http://www.w3.org/2000/svg">
  <defs>
    <linearGradient id="soil-fill" x1="0" y1="0" x2="0" y2="1">
      <stop offset="0" stop-color="var(--soil-dark)"/>
      <stop offset="0.5" stop-color="var(--soil-mid)"/>
      <stop offset="1" stop-color="var(--soil-dark)"/>
    </linearGradient>
    <linearGradient id="grass-top-fill" x1="0" y1="0" x2="0" y2="1">
      <stop offset="0" stop-color="var(--grass-light)"/>
      <stop offset="1" stop-color="var(--grass-deep)"/>
    </linearGradient>
    <linearGradient id="grass-bottom-fill" x1="0" y1="0" x2="0" y2="1">
      <stop offset="0" stop-color="var(--grass-deep)"/>
      <stop offset="1" stop-color="var(--grass-light)"/>
    </linearGradient>
  </defs>

  <rect class="soil-photo" x="0" y="0" width="932" height="1200" fill="url(#soil-fill)" role="img" aria-label="Cross-section of rich brown garden soil"/>
  <rect class="grass-photo-top" x="0" y="0" width="932" height="176" fill="url(#grass-top-fill)" role="img" aria-label="Fresh green lawn grass along the top edge"/>
  <rect class="grass-photo-bottom" x="0" y="1017" width="932" height="183" fill="url(#grass-bottom-fill)" role="img" aria-label="Fresh green lawn grass along the bottom edge"/>

  <text class="brand-name" x="466" y="421" text-anchor="middle" textLength="868" lengthAdjust="spacingAndGlyphs">HADLEYS</text>
  <text class="tagline" x="466" y="519" text-anchor="middle" textLength="752" lengthAdjust="spacingAndGlyphs">full service lawn care</text>
  <text class="web-address" x="466" y="582" text-anchor="middle" textLength="860" lengthAdjust="spacingAndGlyphs">www.hadleygroundskeepingservices.example</text>

  <g class="offer" transform="translate(482 863) rotate(-12)">
    <text class="offer-big" x="0" y="-95" text-anchor="middle" textLength="700" lengthAdjust="spacingAndGlyphs">50%OFF</text>
    <text class="offer-line" x="0" y="-15" text-anchor="middle" textLength="600" lengthAdjust="spacingAndGlyphs">first service</text>
    <text class="offer-line" x="0" y="65" text-anchor="middle" textLength="730" lengthAdjust="spacingAndGlyphs">with seasonal</text>
    <text class="offer-line" x="0" y="140" text-anchor="middle" textLength="390" lengthAdjust="spacingAndGlyphs">service</text>
  </g>
</svg>
</body>
</html>
```